New homepage design - Summit Mentors

- we would like to have a new website layout of the existing one: www.summitmentors-example.ch
the new layout should have the following parameters:
- we want it to be minimalistic
- clear lines
- not too colourful (eventually also more in grey tone?)

our company: summit mentors
- summit mentors is an organizational consulting company and we work with organizations and individuals alike
- we are headquartered in the engadine
- examples: www.bramblequay-example.nyc, www.tallowandfern-example.com, www.corvenhaze-example.com, www.pelldriscoll-example.website,

Target Market(s)

Companies

Industry/Entity Type

Consulting

Number of Pages Required

1 page

Font styles to use
Sans Serif

Colors

Designer to choose only greyscale colors for use in the design.

Requirements
Must have
• A minimalistic design
Nice to have
• minimalistic and slick
Should not have
• not too many colours

```html
<!DOCTYPE html>
<html lang="en">
<head>
<meta charset="utf-8">
<title>Summit Mentors – Turn Purpose into Impact</title>
<link href="https://fonts.googleapis.com/css2?family=Raleway:wght@200;300;400;500;700&display=swap" rel="stylesheet">
<style>
:root{
  --ink:#1c1c1c;
  --text:#4a4a4a;
  --muted:#9a9a9a;
  --band:#7b7b7d;
  --footer:#7a7a7c;
  --tile:#f3f3f3;
  --green:#a8d3a0;
  --white:#ffffff;
  --line:#d9d9d9;
}
*{margin:0;padding:0;box-sizing:border-box}
html,body{width:1200px;height:3431px;overflow:hidden}
body{position:relative;background:var(--white);font-family:"Raleway",sans-serif;color:var(--text)}
.abs{position:absolute}
a{color:inherit;text-decoration:none}

/* header */
.brand{left:50px;top:18px;width:260px;text-align:center;color:var(--ink);white-space:nowrap}
.brand__dot{display:block;margin:0 auto 16px;width:42px;height:42px;border:2px solid var(--ink);border-radius:50%}
.brand__name{font-weight:300;font-size:23px;letter-spacing:.5px;line-height:1}
.brand__tag{font-size:10px;letter-spacing:2.4px;color:var(--muted);margin-top:5px}
.topbar{right:89px;top:10px;display:flex;gap:36px;font-size:13px;color:var(--ink);border-bottom:1px solid var(--line);padding-bottom:8px}
.mainnav{right:89px;top:72px;display:flex;gap:32px;align-items:center;font-size:16px;color:var(--ink)}
.mainnav svg{width:16px;height:16px}

/* hero */
.hero__title{left:88px;top:258px;font-weight:300;font-size:68px;line-height:64px;color:var(--ink);letter-spacing:1px}
.hero__title span{display:block;color:var(--muted);font-weight:200}
.hero__lead{left:89px;top:405px;font-size:15.5px;line-height:24px;color:var(--text)}

/* intro band */
.band{left:0;top:639px;width:1200px;height:498px;background:var(--band)}
.band__photo{left:40px;top:580px;width:580px;height:557px;background:linear-gradient(160deg,#e8eef4 0%,#bccbdb 55%,#8d99a6 100%)}
.section-title{font-weight:300;font-size:45px;line-height:50px;letter-spacing:.5px;white-space:nowrap}
.band__title{left:702px;top:778px;color:var(--white)}
.band__text{left:705px;top:843px;width:410px;font-size:15px;line-height:25px;color:var(--white)}
.arrow{width:34px;height:18px}
.band__arrow{left:704px;top:972px}

/* executive circle */
.circle__title{left:119px;top:1308px;color:var(--ink)}
.circle__text{left:119px;top:1425px;width:410px;font-size:15px;line-height:25px}
.circle__arrow{left:119px;top:1585px}
.hex{clip-path:polygon(50% 0,100% 25%,100% 75%,50% 100%,0 75%,0 25%)}
.tile{width:224px;height:258px;background:var(--tile);display:flex;flex-direction:column;align-items:center;justify-content:center;gap:22px;font-size:17px;color:var(--ink);letter-spacing:.3px}
.tile svg{width:64px;height:64px;stroke:var(--ink);fill:none;stroke-width:2}
.tile--retreats{left:607px;top:1214px}
.tile--hikes{left:858px;top:1214px}
.tile--members{left:732px;top:1429px}

/* testimonials */
.green{left:0;top:1766px;width:1200px;height:498px;background:var(--green)}
.client{left:177px;top:1830px;width:326px;height:377px;background:var(--white);display:flex;align-items:center;justify-content:center;gap:12px}
.client__dot{width:22px;height:22px;border-radius:50%;background:var(--ink)}
.client__name{font-size:30px;font-weight:500;color:var(--ink)}
.quote__title{left:631px;top:1933px;color:var(--white)}
.quote__text{left:631px;top:1998px;width:420px;font-size:15px;line-height:25px;color:var(--white)}
.quote__name{left:631px;top:2096px;font-size:15px;font-weight:700;color:var(--white)}
.quote__role{left:631px;top:2121px;font-size:11px;color:var(--white)}
.dots{left:1112px;top:1989px;display:flex;flex-direction:column;gap:16px}
.dots span{width:9px;height:9px;border-radius:50%;background:rgba(255,255,255,.55)}
.dots span.is-active{background:var(--white)}

/* media */
.media__title{left:86px;top:2560px;color:var(--ink)}
.pager{width:48px;height:52px;background:var(--tile);display:flex;align-items:center;justify-content:center;font-size:16px;color:var(--ink)}
.pager--prev{left:89px;top:2626px}
.pager--next{left:148px;top:2626px}
.card{top:2383px;width:288px;height:436px;background:var(--white);box-shadow:0 18px 40px rgba(0,0,0,.08)}
.card--a{left:517px}
.card--b{left:822px}
.card__photo{width:288px;height:229px}
.card--a .card__photo{background:linear-gradient(180deg,#9aa3a8 0%,#c9b3a2 55%,#d7c6b8 100%)}
.card--b .card__photo{background:linear-gradient(180deg,#d3d6d8 0%,#c7a995 55%,#b1a79f 100%)}
.card__body{padding:21px 24px 0 27px}
.card__date{font-size:11px;color:var(--muted);font-weight:500}
.card__head{margin-top:13px;font-size:13px;line-height:19px;font-weight:700;color:var(--ink)}
.card__text{margin-top:15px;font-size:13px;line-height:22px;color:var(--text)}

/* footer */
.footer{left:0;top:2937px;width:1200px;height:494px;background:var(--footer);color:var(--white)}
.footer .brand{left:62px;top:118px;width:320px}
.footer .brand__dot{width:58px;height:58px;border-color:var(--white);margin-bottom:26px}
.footer .brand__name{font-size:32px;color:var(--white);font-weight:200}
.footer .brand__tag{font-size:12px;color:var(--white);letter-spacing:3px;margin-top:6px}
.fcol{top:86px;font-size:13.5px;line-height:21px}
.fcol h4{font-size:16.5px;font-weight:700;margin-bottom:16px;letter-spacing:.2px}
.fcol--links{left:436px}
.fcol--links li{list-style:none;margin-bottom:10px}
.fcol--address{left:649px}
.fcol--retreats{left:902px;font-size:13px;line-height:22px;white-space:nowrap}
.fcol--retreats strong{display:block;font-size:11px;font-weight:700;letter-spacing:.2px}
.gap{height:14px}
.fdivider{left:89px;top:413px;width:1022px;height:1px;background:rgba(255,255,255,.35)}
.copyright{left:0;top:446px;width:1200px;text-align:center;font-size:12px;font-weight:700}
.totop{left:1129px;top:394px;width:38px;height:44px;background:var(--white);color:var(--footer);display:flex;align-items:center;justify-content:center;font-size:12px}
</style>
</head>
<body>

<header>
  <div class="abs brand">
    <span class="brand__dot"></span>
    <div class="brand__name">SUMMIT MENTORS</div>
    <div class="brand__tag">TURN PURPOSE INTO IMPACT</div>
  </div>
  <nav class="abs topbar"><a>Testimonials</a><a>Recent news</a><a>Contact</a></nav>
  <nav class="abs mainnav">
    <svg viewBox="0 0 16 16"><path d="M8 2 1 8h2v6h4v-4h2v4h4V8h2z" fill="#7b7b7d"/></svg>
    <a>Summit Mentors</a><a>Executive Circle</a><a>For Corporations</a><a>For individuals</a>
  </nav>
</header>

<section class="hero">
  <h1 class="abs hero__title">TURN PURPOSE<span>INTO IMPACT</span></h1>
  <p class="abs hero__lead">We convert the speak of purpose and consciousness into solutions.<br>We are deeply convinced that a life and work ethics</p>
</section>

<section class="intro">
  <div class="abs band"></div>
  <div class="abs band__photo" role="img" aria-label="Photo of a smiling businessman in a light blue shirt and glasses holding an open laptop"></div>
  <h2 class="abs section-title band__title">SUMMIT MENTORS</h2>
  <p class="abs band__text">We convert the speak of purpose and consciousness into solutions. We are deeply convinced that a life and work ethics based on the attitude of serving all stakeholders and developing high levels of inclusiveness...</p>
  <svg class="abs arrow band__arrow" viewBox="0 0 34 18" fill="none" stroke="#fff" stroke-width="2"><path d="M1 9h31M24 1l8 8-8 8"/></svg>
</section>

<section class="circle">
  <h2 class="abs section-title circle__title">THE EXECUTIVE<br>CIRCLE</h2>
  <p class="abs circle__text">The Summit Mentors circle consists of a selected number of C-Level executives, entrepreneurs, politicians, artists and sports people who crave and follow a credible vision, purpose and legacy; this for themselves and for the organizations they lead.</p>
  <svg class="abs arrow circle__arrow" viewBox="0 0 34 18" fill="none" stroke="#1c1c1c" stroke-width="2"><path d="M1 9h31M24 1l8 8-8 8"/></svg>

  <div class="abs hex tile tile--retreats">
    <svg viewBox="0 0 64 64"><circle cx="32" cy="10" r="6"/><circle cx="12" cy="30" r="6"/><circle cx="52" cy="30" r="6"/><circle cx="32" cy="50" r="6"/><path d="M20 14a22 22 0 0 0-6 8M44 14a22 22 0 0 1 6 8M14 42a22 22 0 0 0 8 8M50 42a22 22 0 0 1-8 8"/></svg>
    RETREATS
  </div>
  <div class="abs hex tile tile--hikes">
    <svg viewBox="0 0 64 64"><path d="M4 56 24 20l12 20 8-12 16 28z"/><path d="M24 20l-4 12 6-4 4 6"/></svg>
    INSPIRED HIKES
  </div>
  <div class="abs hex tile tile--members">
    <svg viewBox="0 0 64 64"><circle cx="14" cy="22" r="6"/><circle cx="32" cy="18" r="7"/><circle cx="50" cy="22" r="6"/><path d="M4 52V40a10 10 0 0 1 20 0v12M21 52V38a11 11 0 0 1 22 0v14M40 52V40a10 10 0 0 1 20 0v12"/></svg>
    MEMBER AREA
  </div>
</section>

<section class="testimonials">
  <div class="abs green"></div>
  <div class="abs hex client"><span class="client__dot"></span><span class="client__name">Northfield Labs</span></div>
  <h2 class="abs section-title quote__title">TESTIMONIALS</h2>
  <p class="abs quote__text">The Summit Mentors team enabled me to discuss current and relevant topics in a safe setting, with the group acting as sparring partner and supporter to find solutions.</p>
  <div class="abs quote__name">LUKAS BRENNER</div>
  <div class="abs quote__role">COO, NORTHFIELD LABS</div>
  <div class="abs dots"><span></span><span class="is-active"></span><span></span></div>
</section>

<section class="media">
  <h2 class="abs section-title media__title">MEDIA &amp; PRESS</h2>
  <div class="abs hex pager pager--prev">‹</div>
  <div class="abs hex pager pager--next">›</div>

  <article class="abs card card--a">
    <div class="card__photo" role="img" aria-label="Portrait photo of a smiling dark-haired man in a suit"></div>
    <div class="card__body">
      <div class="card__date">30. OCTOBER 2018</div>
      <h3 class="card__head">BANKER – EIN LEBEN MIT DER GITARRE IN GRENZSITUATIONEN</h3>
      <p class="card__text">Er hat sich zum Spezialisten für festverzinsliche Finanzprodukte und Senior Portfoliomanager...</p>
    </div>
  </article>
  <article class="abs card card--b">
    <div class="card__photo" role="img" aria-label="Portrait photo of a smiling grey-haired man"></div>
    <div class="card__body">
      <div class="card__date">30. OCTOBER 2018</div>
      <h3 class="card__head">EX-KESTREL-TOPMANAGER LEITET «SUMMIT MENTORS»</h3>
      <p class="card__text">An ex-Kestrel private banker is taking over the reins of a network for top executives. The move comes...</p>
    </div>
  </article>
</section>

<footer class="abs footer">
  <div class="abs brand">
    <span class="brand__dot"></span>
    <div class="brand__name">SUMMIT MENTORS</div>
    <div class="brand__tag">TURN PURPOSE INTO IMPACT</div>
  </div>
  <div class="abs fcol fcol--links">
    <h4>QUICK LINKS</h4>
    <ul><li>Summit Mentors</li><li>Executive Circle</li><li>For Corporations</li><li>For individuals</li></ul>
  </div>
  <div class="abs fcol fcol--address">
    <h4>ADDRESS</h4>
    Summit Mentors Ltd.<br>Lindenweg 12<br>7500 St. Moritz
    <div class="gap"></div>
    Telephone: +41 44 000 12 34
    <div class="gap"></div><div class="gap"></div>
    Email: mail@sm-example.ch
  </div>
  <div class="abs fcol fcol--retreats">
    <h4>RETREATS</h4>
    <strong>SUMMIT MENTORS:</strong>
    16.03.2022 – 19.03.2022<br>08.06.2022 – 11.06.2022<br>28.09.2022 – 01.10.2022
    <div class="gap"></div>
    <strong>CLEAR MIND RETREATS</strong>
    02.03.2022 – 05.03.2022 (Level I)<br>14.09.2022 – 17.09.2022 (Level III)
    <div class="gap"></div>
    <strong>TRAIL AND TALK</strong>
    16.06.2022 – 19.06.2022
  </div>
  <div class="abs fdivider"></div>
  <div class="abs copyright">© COPYRIGHT 2022 ALL RIGHTS RESERVED</div>
  <div class="abs hex totop">⌃</div>
</footer>

</body>
</html>
```